We need a business card for a company which is just starting up. The company name is Meridale Executive Services and we do a variety of things such as: support services for executives/leaders, sales team creation/management/training, and implementation of new programs to enhance a company's culture. The final design should be simple, professional and create a buzz of wanting to learn more. The owner is a woman of power, poise and leadership while she maintains qualities of caring, compassionate and honest. Her clients respect and refer her constantly. The colors are up for negotiation but should capture strength and softness at the same time. Possible colors: chocolate brown, dark pink, periwinkle. See attachment.

Target Market(s)

Medium to Large Businesses

Industry/Entity Type

Leadership

Requirements
Nice to have
• Qr code

```html
<!DOCTYPE html>
<html lang="en">
<head>
<meta charset="utf-8">
<title>Meridale Executive Services – Business Card</title>
<link rel="stylesheet" href="https://fonts.googleapis.com/css2?family=Raleway:wght@200;300&family=Noto+Serif:wght@400;700&display=swap">
<style>
  :root {
    --backdrop: #e9e6e2;
    --card: #ffffff;
    --pink: #e8176f;
    --blue: #1e96d6;
    --ink: #2a2a2a;
    --muted: #555555;
    --white: #ffffff;
  }
  * { margin: 0; padding: 0; box-sizing: border-box; }
  html, body {
    width: 1200px;
    height: 1023px;
    overflow: hidden;
    background: var(--backdrop);
  }
  .business-card {
    position: absolute;
    left: 100px;
    top: 226px;
    width: 1000px;
    height: 571px;
    background: var(--card);
    box-shadow: 0 6px 24px rgba(0,0,0,0.12);
    overflow: hidden;
  }
  .brand {
    position: absolute;
    left: 58px;
    top: 130px;
    display: inline-block;
    max-width: 890px;
  }
  .company-name {
    font-family: "Raleway", sans-serif;
    font-weight: 200;
    font-size: 66px;
    line-height: 1.1;
    letter-spacing: -0.5px;
    color: var(--pink);
    white-space: nowrap;
  }
  .tagline {
    margin-top: 6px;
    text-align: right;
    font-family: "Noto Serif", serif;
    font-size: 18px;
    color: var(--ink);
    white-space: nowrap;
  }
  .owner {
    position: absolute;
    left: 62px;
    top: 318px;
    font-family: "Noto Serif", serif;
  }
  .owner-name {
    font-weight: 700;
    font-size: 26px;
    color: var(--pink);
    line-height: 1.1;
  }
  .owner-title {
    font-size: 19px;
    color: var(--muted);
  }
  .contact-band {
    position: absolute;
    left: 0;
    top: 392px;
    width: 100%;
    height: 88px;
    background: var(--blue);
    display: flex;
    align-items: center;
    padding-left: 62px;
    color: var(--white);
    font-family: "Noto Serif", serif;
  }
  .phone-label { font-size: 17px; margin-right: 12px; align-self: flex-end; margin-bottom: 26px; }
  .phone-number {
    font-family: "Raleway", sans-serif;
    font-weight: 300;
    font-size: 44px;
    white-space: nowrap;
  }
  .band-divider {
    width: 1px;
    height: 62px;
    background: rgba(255,255,255,0.7);
    margin: 0 22px 0 28px;
  }
  .web-details { font-size: 17px; line-height: 1.55; white-space: nowrap; }
  .accent-stripe {
    position: absolute;
    left: 0;
    top: 490px;
    width: 100%;
    height: 18px;
    background: var(--pink);
  }
</style>
</head>
<body>
  <div class="business-card">
    <div class="brand">
      <div class="company-name">Meridale Executive Services</div>
      <div class="tagline">support services for executives/leaders</div>
    </div>
    <div class="owner">
      <div class="owner-name">Rosalind Avery</div>
      <div class="owner-title">Owner</div>
    </div>
    <div class="contact-band">
      <span class="phone-label">telephone:</span>
      <span class="phone-number">(555) 555-5555</span>
      <span class="band-divider"></span>
      <div class="web-details">
        <div>email: rosalind@email.com</div>
        <div>website: www.meridaleexec.com</div>
      </div>
    </div>
    <div class="accent-stripe"></div>
  </div>
</body>
</html>
```